Unique and original Business Card for Financial Services Business

I have moved premises and need to change the detail on my business card so thought now is a good time for a re-design. Looking for something professional and modern with colours to fit in with out logo. Like the idea of foil or embossing if that works but not a must have but I do want something that stands out and that I could not design myself.

Once business card is designed I will also be looking to get letterhead and flyers done but want the business card concept in place first.

The majority of designs I am receiving are generic and template based. I am looking for something unique and original. We have some great design elements in our logo, think outside the box and show me something that stands out from the crowd.

Target Market(s)

Business Professionals

Industry/Entity Type

Finance

Contact Information for Business Card

Name: Delia Norwood Phone 0473 958 162 Address PO Box 8617 Mossvale NSW 2389 Email info@steadyharbourfinancialservices.com.au website www.steadyharbourfinancialservices.com.au

Font styles to use
Other font styles liked:
• Ralway

Requirements
Should not have
• No black backgrounds please

```html
<!DOCTYPE html>
<html lang="en">
<head>
<meta charset="utf-8">
<title>Steady Harbour Financial Services – Business Card</title>
<link href="https://fonts.googleapis.com/css2?family=Raleway:wght@400;500;700&display=swap" rel="stylesheet">
<style>
  :root {
    --backdrop: #e7e3df;
    --card: #f3f3f2;
    --card-edge: #d9d9d8;
    --teal: #1f7b78;
    --teal-deep: #236a6e;
    --teal-soft: #4a9c92;
    --ink: #1f1f1f;
    --ink-soft: #444;
  }
  * { box-sizing: border-box; margin: 0; padding: 0; }
  html, body {
    width: 1200px; height: 900px; overflow: hidden;
    background: var(--backdrop);
    font-family: "Raleway", sans-serif;
  }
  .business-card {
    position: absolute; left: 150px; top: 192px;
    width: 900px; height: 517px;
    background: var(--card);
    border: 1px solid var(--card-edge);
    border-radius: 22px;
    overflow: hidden;
    box-shadow: 0 10px 30px rgba(0,0,0,0.08);
  }
  .bird-illustration {
    position: absolute; left: 0; top: 0;
    width: 440px; height: 100%;
    background: linear-gradient(100deg, var(--teal-soft) 0%, var(--teal-deep) 38%, rgba(35,106,110,0.45) 62%, rgba(243,243,242,0) 100%);
  }
  .brand {
    position: absolute; right: 46px; top: 62px;
    text-align: right;
    color: var(--ink-soft);
    font-weight: 400;
  }
  .brand-square {
    display: inline-block;
    width: 70px; height: 70px;
    background: var(--teal);
    margin-bottom: 34px;
    margin-right: 120px;
  }
  .brand-name {
    font-size: 40px; line-height: 1; letter-spacing: 0.5px;
  }
  .brand-tagline {
    font-size: 25px; line-height: 1.1; letter-spacing: 7.5px;
    margin-right: -7px;
  }
  .person {
    position: absolute; right: 46px; top: 266px;
    text-align: right;
  }
  .person-name {
    color: var(--teal);
    font-size: 36px; font-weight: 700; letter-spacing: 1px; line-height: 1.2;
  }
  .person-role {
    color: var(--ink);
    font-size: 20px; font-weight: 500; margin-top: 4px;
  }
  .contact-list {
    position: absolute; right: 40px; top: 362px;
    list-style: none;
  }
  .contact-item {
    display: flex; justify-content: flex-end; align-items: center;
    height: 29px;
    font-size: 19px; color: var(--ink); font-weight: 500;
  }
  .contact-item.phone { font-weight: 700; }
  .contact-icon { width: 16px; height: 16px; margin-left: 14px; fill: var(--teal); }
</style>
</head>
<body>
  <div class="business-card">
    <div class="bird-illustration" role="img" aria-label="Teal hummingbird illustration in flight with silver foil outline"></div>

    <div class="brand">
      <span class="brand-square"></span>
      <div class="brand-name">STEADY HARBOUR</div>
      <div class="brand-tagline">Financial Services</div>
    </div>

    <div class="person">
      <div class="person-name">DELIA NORWOOD</div>
      <div class="person-role">Founder &amp; CEO</div>
    </div>

    <ul class="contact-list">
      <li class="contact-item phone">0473 958 162
        <svg class="contact-icon" viewBox="0 0 24 24"><path d="M6.6 10.8a15 15 0 0 0 6.6 6.6l2.2-2.2a1 1 0 0 1 1-.25 11.4 11.4 0 0 0 3.6.57 1 1 0 0 1 1 1V20a1 1 0 0 1-1 1A17 17 0 0 1 3 4a1 1 0 0 1 1-1h3.5a1 1 0 0 1 1 1c0 1.25.2 2.45.57 3.57a1 1 0 0 1-.25 1z"/></svg>
      </li>
      <li class="contact-item">info@steadyharbourfinancialservices.com.au
        <svg class="contact-icon" viewBox="0 0 24 24"><path d="M3 5h18a1 1 0 0 1 1 1v12a1 1 0 0 1-1 1H3a1 1 0 0 1-1-1V6a1 1 0 0 1 1-1zm9 7.5L4 7.5V9l8 5 8-5V7.5z"/></svg>
      </li>
      <li class="contact-item">www.steadyharbourfinancialservices.com.au
        <svg class="contact-icon" viewBox="0 0 24 24"><circle cx="12" cy="12" r="10"/><path d="M2 12h20M12 2c3 3 3 17 0 20M12 2c-3 3-3 17 0 20" stroke="#f3f3f2" stroke-width="1.5" fill="none"/></svg>
      </li>
      <li class="contact-item">PO Box 8617 Mossvale, NSW 2389
        <svg class="contact-icon" viewBox="0 0 24 24"><path d="M12 2a7 7 0 0 0-7 7c0 5 7 13 7 13s7-8 7-13a7 7 0 0 0-7-7zm0 9.5A2.5 2.5 0 1 1 12 6.5a2.5 2.5 0 0 1 0 5z"/></svg>
      </li>
    </ul>
  </div>
</body>
</html>
```